Business Card Design Project

We are looking to redesign the logo, business card and stationary of one of our group companies - KESTRAL SUPPLY COMPANY LLC.

The company specialises in industrial PVC and CPVC Piping systems. It is situated in the Middle East and the focus is purely in this region.

The logo work is already completed. The file is uploaded for the reference.

We are looking for a clean minimalistic design for the business card.

regards
Dorun

Hello Everyone!

Thanks for submitting your designs. 

Yet to find the right design. Probably the below links will give you guys some more idea on what we would like.

Minimalist design with some creativity.

Dorun

http://pixelorchard-example.com/inspiration/15-beautifully-minimal-business-cards

http://www.graphvane-example.com/2011/11/14/30-minimalist-business-card-design/

http://www.topdrafthub-example.com/inspiration/minimal-business-cards/

Target Market(s)

Industrial users

Industry/Entity Type

Industrial

Requirements
Must have
• - Minimalistic design

- Back side of the card should include the manufacturer PLUMARC CANADA's decal. The file is upload for the reference

- Further information
Company Name:
KESTRAL SUPPLY COMPANY LLC
Address:
PO Box 3857, Sharjah Industrial Area 5, Tarvesh Road
Sharjah, United Arab Emirates
Telephone:
+971-6-5000-912
Fax:
+977-6-5000-913
Email:
mail@ksqholdings.com

- FYI, Kestral Supply Company LLC is the authorised distributor for PLUMARC CANADA in the UAE. For further information on plumarc please visit the website www.plumarc.ca

```html
<!DOCTYPE html>
<html lang="en">
<head>
<meta charset="utf-8">
<title>Kestral Supply Company LLC – Business Card</title>
<link rel="stylesheet" href="https://fonts.googleapis.com/css2?family=Mulish:wght@400;600;700&display=swap">
<style>
  :root {
    --backdrop: #3a3a39;
    --card: #f3f4f4;
    --card-edge: #e6e8e8;
    --ink: #6f6f6f;
    --ink-soft: #7c7c7c;
    --accent: #5279c0;
    --accent-deep: #3f63ad;
  }
  * { box-sizing: border-box; margin: 0; padding: 0; }
  html, body { width: 1200px; height: 960px; overflow: hidden; }
  body {
    background: var(--backdrop);
    font-family: "Mulish", "Helvetica Neue", Arial, sans-serif;
    color: var(--ink);
    position: relative;
  }
  .card {
    position: absolute;
    top: 319px;
    width: 450px;
    height: 243px;
    border-radius: 18px;
    background: radial-gradient(ellipse at 45% 40%, #fbfbfb 0%, var(--card) 55%, var(--card-edge) 100%);
    overflow: hidden;
  }
  .card--front { left: 106px; }
  .card--back { left: 644px; }

  .edge-tab {
    position: absolute;
    width: 12px;
    height: 46px;
    top: 99px;
    background: var(--accent);
  }
  .card--front .edge-tab { right: 0; }
  .card--back .edge-tab { left: 0; }

  /* Front: company name */
  .brand {
    position: absolute;
    left: 110px;
    top: 88px;
    display: flex;
    align-items: center;
    gap: 12px;
  }
  .brand__mark {
    width: 62px;
    height: 62px;
    border-radius: 16px;
    background: var(--accent);
  }
  .brand__name {
    font-weight: 600;
    color: var(--ink-soft);
    line-height: 1;
  }
  .brand__name-main {
    display: block;
    font-size: 38px;
    letter-spacing: 0.5px;
  }
  .brand__name-sub {
    display: block;
    font-size: 9.5px;
    letter-spacing: 4.2px;
    margin-top: 4px;
  }

  /* Back: person and contact */
  .person {
    position: absolute;
    left: 37px;
    top: 28px;
  }
  .person__name {
    font-size: 22px;
    font-weight: 700;
    color: var(--ink);
    line-height: 1.05;
  }
  .person__role {
    font-size: 17px;
    font-weight: 400;
    color: var(--ink-soft);
    line-height: 1.1;
  }
  .contact {
    position: absolute;
    left: 37px;
    top: 98px;
    list-style: none;
    font-size: 13px;
    line-height: 16px;
    color: var(--ink-soft);
  }
  .contact b { font-weight: 700; color: var(--ink); }
  .address {
    position: absolute;
    left: 37px;
    bottom: 15px;
    font-size: 9.6px;
    color: var(--ink-soft);
    white-space: nowrap;
  }
  .corner-block {
    position: absolute;
    left: 350px;
    top: 4px;
    width: 112px;
    height: 112px;
    border-radius: 26px;
    background: linear-gradient(160deg, var(--accent) 0%, var(--accent-deep) 100%);
  }
</style>
</head>
<body>
  <section class="card card--front" aria-label="Card front">
    <div class="brand">
      <span class="brand__mark"></span>
      <span class="brand__name">
        <span class="brand__name-main">KESTRAL</span>
        <span class="brand__name-sub">SUPPLY CO. LLC</span>
      </span>
    </div>
    <span class="edge-tab"></span>
  </section>

  <section class="card card--back" aria-label="Card back">
    <span class="edge-tab"></span>
    <div class="person">
      <p class="person__name">Your Name</p>
      <p class="person__role">Managing Director</p>
    </div>
    <ul class="contact">
      <li><b>T:</b> +971-6-5000-912</li>
      <li><b>F:</b> +977-6-5000-913</li>
      <li><b>E:</b> mail@ksqholdings.com</li>
    </ul>
    <p class="address">PO Box 3857 | Industrial Area 5, Tarvesh Road | Sharjah | United Arab Emirates</p>
    <span class="corner-block"></span>
  </section>
</body>
</html>
```